App UI design needed! For a Password Management Tool

Need a design of a Windows desktop application which is a Password Management Tool, similar to Vaultrixa, Kelmorin or Tibruna, with Business/Enterprise functionalities. Here attached are a few sample pages of Kelmorin, and some sample pages of our app called Quendly. We certainly want to redesign our app.
We need: 1. The layout of the web: top banner, menu, main pane; 2. Form style, main form and sub forms; 3. List style; 4 Fonts and buttons; 5. Logo.
The design should look professional, can attract business customers as well as individual users, and present a strong sense of “Security”. The look and feel should differentiate from well-known products like Vaultrixa, Kelmorin, Tibruna, etc.

```html
<!DOCTYPE html>
<html lang="en">
<head>
<meta charset="utf-8">
<title>Quendly – Web Logins</title>
<link rel="stylesheet" href="https://fonts.googleapis.com/css2?family=Inter:wght@400;500;600&display=swap">
<style>
:root{
  --bg:#15133a;
  --panel:#24224d;
  --card:#17153a;
  --band:#1f1d46;
  --row-hover:#2c2a57;
  --text:#ffffff;
  --muted:#c9c8dc;
  --soft:#9f9dbd;
  --line:#34325c;
  --accent:#0a8cff;
  --green:#20d98a;
}
*{box-sizing:border-box;margin:0;padding:0}
html,body{width:1200px;height:750px;overflow:hidden}
body{background:var(--bg);font-family:"Inter",sans-serif;color:var(--text);position:relative}
.abs{position:absolute}
.brand{left:16px;top:33px;width:153px;height:33px;background:#2a3440;display:flex;align-items:center;gap:7px;padding-left:8px;font-size:17px;font-weight:600;color:var(--accent)}
.brand-dot{width:16px;height:16px;border-radius:50%;background:var(--accent)}
.search{left:240px;top:30px;width:480px;height:39px;border-radius:8px;background:#262450;display:flex;align-items:center;justify-content:space-between;padding:0 14px 0 25px;font-size:13px;color:var(--muted)}
.top-icon{top:38px}
.avatar{left:1107px;top:33px;width:35px;height:35px;border-radius:50%;background:radial-gradient(circle at 50% 40%,#8a6a55,#3a2a22);border:2px solid var(--accent)}
.nav{left:10px;top:0;width:220px}
.nav-item{position:absolute;left:0;width:220px;height:52px;display:flex;align-items:center;gap:14px;padding-left:13px;font-size:14px;font-weight:500;color:var(--muted)}
.nav-item.active{border:1px solid var(--accent);border-radius:8px;background:#24224d;color:var(--text);font-weight:600}
.version{left:16px;top:729px;font-size:12px;color:var(--muted)}
.main{left:240px;top:101px;width:960px;height:649px;background:var(--panel);border-radius:12px 0 0 0}
.title{left:267px;top:119px;font-size:19px;font-weight:600}
.subtitle{left:267px;top:145px;font-size:13px;color:var(--muted)}
.btn-new{left:1046px;top:114px;width:113px;height:45px;border-radius:6px;background:var(--accent);display:flex;align-items:center;justify-content:center;gap:8px;font-size:14px;font-weight:600;box-shadow:0 12px 24px rgba(10,140,255,.25)}
.list{left:267px;top:182px;width:896px;height:547px;background:var(--card);border-radius:10px}
.list-title{left:291px;top:204px;font-size:18px;font-weight:600}
.count{left:647px;top:207px;font-size:11.5px;color:var(--muted)}
.pager{left:1045px;top:207px;font-size:11.5px;color:var(--muted);word-spacing:14px}
.band{left:267px;top:240px;width:896px;height:43px;background:var(--band)}
.head{top:251px;font-size:13px;font-weight:500;color:var(--muted)}
.check{position:absolute;left:292px;width:16px;height:16px;border:1.5px solid var(--soft);border-radius:3px}
.row-hl{left:277px;top:344px;width:876px;height:51px;border-radius:6px;background:var(--row-hover)}
.cell{position:absolute;font-size:13px;font-weight:500;color:var(--muted);transform:translateY(-50%)}
.cell.name{left:329px;display:flex;align-items:center;gap:10px;color:var(--text);font-weight:600}
.cell.user{left:519px}
.cell.url{left:750px}
.mark{width:22px;height:22px;border-radius:50%}
.hl .cell{color:var(--text);font-weight:600}
.divider{left:291px;width:862px;height:1px;background:var(--line)}
.act{top:353px}
.open-btn{left:996px;top:351px;width:38px;height:38px;border-radius:50%;background:#55557a;display:flex;align-items:center;justify-content:center}
.tooltip{left:984px;top:392px;width:57px;height:26px;border-radius:4px;background:#3b3a63;font-size:13px;display:flex;align-items:center;justify-content:center}
</style>
</head>
<body>
<div class="abs brand"><span class="brand-dot"></span>Quendly</div>
<div class="abs search">Find something...
  <svg width="18" height="18" viewBox="0 0 18 18" fill="none" stroke="#c9c8dc" stroke-width="1.5"><circle cx="8" cy="8" r="6.5"/><path d="M13 13l4 4"/></svg>
</div>
<svg class="abs top-icon" style="left:950px" width="22" height="24" viewBox="0 0 22 24"><path d="M11 2a6 6 0 0 0-6 6v5l-2 4h16l-2-4V8a6 6 0 0 0-6-6z" fill="#0a8cff"/><circle cx="11" cy="20" r="2.5" fill="#0a8cff"/><circle cx="18" cy="4" r="3" fill="#20d98a"/></svg>
<svg class="abs top-icon" style="left:1032px" width="22" height="22" viewBox="0 0 24 24"><path fill="#0a8cff" d="M10 1h4l.6 3 2.4 1.2 2.6-1.6 2.8 2.8-1.6 2.6L22 11v2l-3 .6-1.2 2.4 1.6 2.6-2.8 2.8-2.6-1.6L14 20v3h-4l-.6-3-2.4-1.2-2.6 1.6-2.8-2.8 1.6-2.6L2 13v-2l3-.6 1.2-2.4L4.6 5.4l2.8-2.8 2.6 1.6L10 4z"/><circle cx="12" cy="12" r="3.5" fill="#15133a"/></svg>
<div class="abs avatar" role="img" aria-label="User profile photo"></div>
<svg class="abs" style="left:1154px;top:47px" width="10" height="7" viewBox="0 0 10 7"><path d="M0 0h10L5 7z" fill="#20d98a"/></svg>

<nav class="abs nav">
  <div class="nav-item" style="top:104px"><svg width="20" height="20"><rect x="0" y="0" width="8" height="9" rx="2" fill="#0a8cff"/><rect x="0" y="11" width="8" height="9" rx="2" fill="#20d98a"/><rect x="11" y="0" width="8" height="20" rx="2" fill="#8ea0ff"/></svg>Dashboard</div>
  <div class="nav-item" style="top:155px"><svg width="20" height="20"><circle cx="10" cy="6" r="4.5" fill="#0a8cff"/><path d="M2 19c0-5 4-7 8-7s8 2 8 7z" fill="#0a8cff"/></svg>Users</div>
  <div class="nav-item" style="top:205px"><svg width="20" height="20"><circle cx="8" cy="6" r="4" fill="#0a8cff"/><path d="M0 18c0-5 4-6 8-6s8 1 8 6z" fill="#0a8cff"/><circle cx="15" cy="7" r="3" fill="#20d98a"/></svg>Teams</div>
  <div class="nav-item" style="top:256px"><svg width="20" height="20"><rect x="0" y="0" width="10" height="7" rx="2" fill="#0a8cff"/><rect x="9" y="12" width="10" height="7" rx="2" fill="#0a8cff"/><path d="M4 7v8h5" stroke="#20d98a" stroke-width="2" fill="none"/></svg>Client Containers</div>
  <div class="nav-item active" style="top:309px"><svg width="20" height="20" viewBox="0 0 20 20" fill="none" stroke="#20d98a" stroke-width="1.8"><circle cx="10" cy="10" r="8.5" fill="#20d98a" fill-opacity=".25"/><path d="M1.5 10h17M10 1.5c-4 4-4 13 0 17M10 1.5c4 4 4 13 0 17"/></svg>Web Logins</div>
  <div class="nav-item" style="top:357px"><svg width="20" height="20"><path d="M3 0h10l5 5v15H3z" fill="#0a8cff"/><path d="M6 10h9M6 13h9M6 16h6" stroke="#15133a" stroke-width="1.5"/></svg>Reports</div>
</nav>
<div class="abs version">Version 2.3.4</div>

<main class="abs main"></main>
<h1 class="abs title">Web Logins</h1>
<p class="abs subtitle">Showing details of all the web logins saved in your system</p>
<div class="abs btn-new"><svg width="13" height="13"><path d="M6.5 0v13M0 6.5h13" stroke="#fff" stroke-width="2"/></svg>New</div>

<section class="abs list"></section>
<h2 class="abs list-title">Lists</h2>
<div class="abs count">Showing 1-10 of 354 items</div>
<div class="abs pager">Page 1 / 36</div>
<div class="abs band"></div>
<span class="check" style="top:249px"></span>
<span class="abs head" style="left:329px">Name</span>
<span class="abs head" style="left:519px">User name</span>
<span class="abs head" style="left:749px">Login page URL</span>

<div class="abs row-hl"></div>
<div class="abs divider" style="top:460px"></div>
<div class="abs divider" style="top:527px"></div>

<div class="row">
  <span class="check" style="top:305px"></span>
  <span class="cell name" style="top:313px"><span class="mark" style="background:#1877f2"></span>Friendlane</span>
  <span class="cell user" style="top:313px">lmarsh@mailbeam.com</span>
  <span class="cell url" style="top:313px">https://www.friendlane.com</span>
</div>
<div class="row hl">
  <span class="check" style="top:361px"></span>
  <span class="cell name" style="top:369px"><span class="mark" style="background:#ffffff"></span>Codeharbor</span>
  <span class="cell user" style="top:369px">lmarsh@mailbeam.com</span>
  <span class="cell url" style="top:369px">https://www.codeharbor.com/login</span>
</div>
<div class="row">
  <span class="check" style="top:418px"></span>
  <span class="cell name" style="top:426px"><span class="mark" style="background:#e84b3c"></span>Searchly</span>
  <span class="cell user" style="top:426px">lmarsh@mailbeam.com</span>
  <span class="cell url" style="top:426px">https://exchange.tolvaro.com</span>
</div>
<div class="row">
  <span class="check" style="top:488px"></span>
  <span class="cell name" style="top:496px"><span class="mark" style="background:#1877f2"></span>Friendlane</span>
  <span class="cell user" style="top:496px">lmarsh12@mailbeam.com</span>
  <span class="cell url" style="top:496px">https://www.friendlane.com</span>
</div>
<div class="row">
  <span class="check" style="top:547px"></span>
  <span class="cell name" style="top:555px"><span class="mark" style="background:#f5a623"></span>Shopvane</span>
  <span class="cell user" style="top:555px">lmarsh@mailbeam.com</span>
  <span class="cell url" style="top:555px">https://www.shopvane.com</span>
</div>

<div class="abs open-btn"><svg width="18" height="18" viewBox="0 0 18 18" fill="none" stroke="#fff" stroke-width="1.5"><path d="M1 5V1h4M13 1h4v4M17 13v4h-4M5 17H1v-4"/><circle cx="6.5" cy="9" r="2"/><path d="M8.5 9h5v2"/></svg></div>
<svg class="abs" style="left:1030px;top:374px" width="14" height="18" viewBox="0 0 14 18"><path d="M1 1v14l4-4 3 6 2-1-3-6h5z" fill="#fff" stroke="#15133a" stroke-width=".8"/></svg>
<svg class="abs act" style="left:1064px" width="18" height="18" viewBox="0 0 18 18" fill="none" stroke="#fff" stroke-width="1.5"><path d="M8 3H2v13h13v-6"/><path d="M14 1l3 3-8 8H6V9z"/></svg>
<svg class="abs act" style="left:1111px" width="16" height="18" viewBox="0 0 16 18"><path d="M1 3h14M6 3V1h4v2" stroke="#fff" stroke-width="1.5" fill="none"/><path d="M2.5 5h11l-1 12h-9z" fill="#fff"/></svg>
<div class="abs tooltip">Open</div>
</body>
</html>
```